Ashcombe Ridge Business Cards

We need business card designs for a modern home development, Ashcombe Ridge. We would like to see modern looking designs- clean and simple but striking. I've attached some images of one of the homes so you can see the style of the homes we are putting on the market and perhaps they will inspire your design! I've also attached the logo- both horizontal and vertical. We need to use the logo on the card. I've also attached a sign that has a map of the development. If you can use that and still keep the card nice and clean, great. If not, it's not a problem to leave the map out completely.

```html
<!DOCTYPE html>
<html lang="en">
<head>
<meta charset="utf-8">
<title>Ashcombe Ridge Business Cards</title>
<link rel="stylesheet" href="https://fonts.googleapis.com/css2?family=Montserrat:wght@400;600;800&family=Oswald:wght@400;500&display=swap">
<style>
  :root {
    --page: #e9e6e1;
    --card: #ffffff;
    --teal: #0a8aa0;
    --teal-soft: #cfe3e8;
    --charcoal: #3a3a3c;
    --ink: #2d2d2f;
    --muted: #6b6b6e;
  }
  * { box-sizing: border-box; margin: 0; padding: 0; }
  html, body { width: 1057px; height: 1200px; overflow: hidden; }
  body {
    background: var(--page);
    font-family: "Montserrat", Arial, sans-serif;
    color: var(--ink);
    position: relative;
  }
  .card-set { position: absolute; left: 60px; width: 937px; height: 540px; }
  .card-set--front { top: 45px; }
  .card-set--back { top: 625px; }

  .card-reverse {
    position: absolute; left: 37px; top: 0;
    width: 900px; height: 514px;
    background: var(--teal);
    box-shadow: 0 6px 18px rgba(0,0,0,.18);
  }
  .card {
    position: absolute; left: 0; top: 26px;
    width: 900px; height: 514px;
    background: var(--card);
    box-shadow: 0 8px 24px rgba(0,0,0,.22);
    overflow: hidden;
  }

  .band {
    position: absolute; left: 0; right: 0; bottom: 70px; height: 58px;
    background: var(--charcoal);
    display: flex; align-items: center; justify-content: center;
    color: #fff; font-size: 21px; letter-spacing: 4px;
  }

  .brand {
    position: absolute; display: flex; align-items: center; gap: 14px;
  }
  .brand__square { width: 34px; height: 34px; background: var(--teal); }
  .brand__name {
    font-weight: 800; font-size: 34px; letter-spacing: 1px;
    color: var(--ink); text-transform: uppercase; line-height: 1;
  }

  .card--front .brand { left: 50%; top: 150px; transform: translateX(-50%); }

  .card--back .brand { left: 60px; top: 268px; }
  .card--back .brand__name { font-size: 28px; }
  .card--back .brand__square { width: 28px; height: 28px; }
  .card--back .band { justify-content: flex-end; padding-right: 70px; font-size: 18px; letter-spacing: 2px; }

  .rule { position: absolute; height: 6px; background: var(--teal); }
  .rule--top { left: 0; top: 120px; width: 380px; }
  .rule--bottom { right: 0; top: 330px; width: 300px; }

  .person { position: absolute; left: 440px; top: 46px; }
  .person__name {
    font-family: "Oswald", Arial, sans-serif; font-weight: 500;
    font-size: 46px; letter-spacing: 3px; text-transform: uppercase; line-height: 1;
  }
  .person__role {
    font-size: 17px; letter-spacing: 3px; text-transform: uppercase;
    color: var(--muted); margin-top: 8px;
  }

  .contacts { position: absolute; left: 440px; top: 150px; list-style: none; }
  .contacts li {
    display: flex; align-items: center; gap: 14px;
    font-size: 16px; color: var(--ink); height: 38px;
  }
  .contacts svg { width: 24px; height: 24px; flex: none; }
</style>
</head>
<body>

<section class="card-set card-set--front">
  <div class="card-reverse"></div>
  <article class="card card--front">
    <div class="brand">
      <span class="brand__square"></span>
      <span class="brand__name">Ashcombe Ridge</span>
    </div>
    <div class="band">www.ashcomberidge.com</div>
  </article>
</section>

<section class="card-set card-set--back">
  <div class="card-reverse"></div>
  <article class="card card--back">
    <div class="rule rule--top"></div>
    <div class="rule rule--bottom"></div>

    <div class="person">
      <h1 class="person__name">Daniel Hartley</h1>
      <p class="person__role">General Manager</p>
    </div>

    <ul class="contacts">
      <li>
        <svg viewBox="0 0 24 24"><rect width="24" height="24" rx="3" fill="#3a3a3c"/><path d="M8 6l2.5 0 1 3-1.5 1.2a7 7 0 0 0 3.8 3.8L15 12.5l3 1V16a1.5 1.5 0 0 1-1.6 1.5A10.5 10.5 0 0 1 6.5 7.6 1.5 1.5 0 0 1 8 6z" fill="#fff"/></svg>
        014 552 0183
      </li>
      <li>
        <svg viewBox="0 0 24 24"><rect width="24" height="24" rx="3" fill="#3a3a3c"/><rect x="8" y="5" width="8" height="14" rx="1.5" fill="none" stroke="#fff" stroke-width="1.6"/><circle cx="12" cy="16.5" r="0.9" fill="#fff"/></svg>
        014 552 0184
      </li>
      <li>
        <svg viewBox="0 0 24 24"><rect width="24" height="24" rx="3" fill="#3a3a3c"/><rect x="5" y="7" width="14" height="10" fill="none" stroke="#fff" stroke-width="1.6"/><path d="M5 7l7 6 7-6" fill="none" stroke="#fff" stroke-width="1.6"/></svg>
        hello@ashcomberidge.com
      </li>
      <li>
        <svg viewBox="0 0 24 24"><rect width="24" height="24" rx="3" fill="#3a3a3c"/><circle cx="12" cy="12" r="6.5" fill="none" stroke="#fff" stroke-width="1.5"/><path d="M5.5 12h13M12 5.5c-3 3.5-3 9.5 0 13M12 5.5c3 3.5 3 9.5 0 13" fill="none" stroke="#fff" stroke-width="1.2"/></svg>
        www.ashcomberidge.com
      </li>
    </ul>

    <div class="brand">
      <span class="brand__square"></span>
      <span class="brand__name">Ashcombe Ridge</span>
    </div>

    <div class="band">42 Fernhill Road, Unit 3, North Block</div>
  </article>
</section>

</body>
</html>
```